design of wedding invitations

I'm looking for someone to design a wedding invitation template/card , 5''x7'' size, must be unique, elegant, classy and original, something that stands out! We may pick more than one, be creative!

wedding date August 17th
names Emily & Kenan

```html
<!DOCTYPE html>
<html lang="en">
<head>
<meta charset="utf-8">
<title>Wedding Invitation – Emily &amp; Kenan</title>
<link rel="stylesheet" href="https://fonts.googleapis.com/css2?family=Cormorant+Garamond:ital,wght@1,600&family=Great+Vibes&family=Open+Sans:wght@300;400&display=swap">
<style>
  :root {
    --marble-light: #f7f7f8;
    --marble-mid: #dcdde0;
    --marble-vein: #b9bbc0;
    --foliage-deep: #3f5587;
    --foliage-soft: #8ea0c9;
    --ink: #1d1d22;
    --gold-light: #f1dc9a;
    --gold: #c79b3c;
    --gold-dark: #8c6620;
    --frame-white: #ffffff;
  }
  html, body {
    margin: 0;
    padding: 0;
    width: 1040px;
    height: 1200px;
    overflow: hidden;
    background: var(--marble-light);
  }
  .invitation {
    position: relative;
    width: 1040px;
    height: 1200px;
    overflow: hidden;
  }
  .invitation__art {
    position: absolute;
    inset: 0;
    width: 1040px;
    height: 1200px;
  }
  .invitation__text {
    position: absolute;
    left: 0;
    width: 1040px;
    margin: 0;
    text-align: center;
    color: var(--ink);
    white-space: nowrap;
  }
  .heading-wedding {
    top: 352px;
    font-family: "Cormorant Garamond", Georgia, serif;
    font-style: italic;
    font-weight: 600;
    font-size: 50px;
    letter-spacing: 4px;
  }
  .heading-invitation {
    top: 418px;
    font-family: "Open Sans", Arial, sans-serif;
    font-weight: 300;
    font-size: 42px;
    letter-spacing: 1px;
  }
  .couple-names {
    top: 470px;
    font-family: "Great Vibes", cursive;
    font-size: 84px;
    line-height: 1.2;
    background: linear-gradient(180deg, var(--gold-light) 0%, var(--gold) 50%, var(--gold-dark) 100%);
    -webkit-background-clip: text;
    background-clip: text;
    color: transparent;
  }
  .wedding-date {
    top: 585px;
    font-family: "Great Vibes", cursive;
    font-size: 56px;
  }
  .venue-street {
    top: 660px;
    font-family: "Open Sans", Arial, sans-serif;
    font-size: 34px;
  }
  .venue-country {
    top: 704px;
    font-family: "Open Sans", Arial, sans-serif;
    font-size: 34px;
  }
</style>
</head>
<body>
<main class="invitation">
  <svg class="invitation__art" viewBox="0 0 1040 1200" xmlns="http://www.w3.org/2000/svg">
    <defs>
      <linearGradient id="marble-fill" x1="0" y1="0" x2="1" y2="1">
        <stop offset="0" stop-color="var(--marble-light)"/>
        <stop offset="0.45" stop-color="var(--marble-mid)"/>
        <stop offset="0.7" stop-color="var(--marble-light)"/>
        <stop offset="1" stop-color="var(--marble-vein)"/>
      </linearGradient>
      <linearGradient id="foliage-fill" x1="0" y1="0" x2="1" y2="1">
        <stop offset="0" stop-color="var(--foliage-soft)"/>
        <stop offset="1" stop-color="var(--foliage-deep)"/>
      </linearGradient>
    </defs>

    <rect class="marble-surface" role="img" aria-label="White and grey marble texture background" x="0" y="0" width="1040" height="1200" fill="url(#marble-fill)"/>

    <g class="foliage-top-left" role="img" aria-label="Watercolour blue leaves and sprigs along the upper left edge of the frame">
      <ellipse cx="360" cy="380" rx="190" ry="70" transform="rotate(-40 360 380)" fill="url(#foliage-fill)" opacity="0.85"/>
    </g>
    <g class="foliage-top-right" role="img" aria-label="Watercolour blue leafy stem along the upper right edge of the frame">
      <ellipse cx="800" cy="340" rx="200" ry="55" transform="rotate(42 800 340)" fill="url(#foliage-fill)" opacity="0.8"/>
    </g>
    <g class="foliage-bottom-left" role="img" aria-label="Large watercolour blue leaf with smaller sprigs at the lower left of the frame">
      <ellipse cx="330" cy="900" rx="210" ry="85" transform="rotate(40 330 900)" fill="url(#foliage-fill)" opacity="0.9"/>
    </g>
    <g class="foliage-bottom-right" role="img" aria-label="Watercolour blue leafy stem along the lower right edge of the frame">
      <ellipse cx="790" cy="880" rx="230" ry="60" transform="rotate(-42 790 880)" fill="url(#foliage-fill)" opacity="0.8"/>
    </g>

    <g class="diamond-frame">
      <polygon class="diamond-frame__panel" points="520,190 880,545 520,900 160,545" fill="var(--frame-white)"/>
      <polygon class="diamond-frame__outline" points="520,160 905,545 520,930 135,545" fill="none" stroke="var(--frame-white)" stroke-width="4"/>
      <polygon class="diamond-frame__outline" points="520,140 925,545 520,950 115,545" fill="none" stroke="var(--frame-white)" stroke-width="2"/>
    </g>
  </svg>

  <p class="invitation__text heading-wedding">WEDDING</p>
  <p class="invitation__text heading-invitation">INVITATION</p>
  <h1 class="invitation__text couple-names">Emily &amp; Kenan</h1>
  <p class="invitation__text wedding-date">August 17th</p>
  <p class="invitation__text venue-street">Maple Avenue, 1720</p>
  <p class="invitation__text venue-country">USA</p>
</main>
</body>
</html>
```